Zielgruppe
Steuerberater, Zielgruppe: Mandanten
Aufgabenstellung
Es sollten keine Balken an den Rändern vorhanden sein, so dass das Briefpapier mit dem eigenen Farbdrucker bedruckt werden kann.
-Keine Balken an den Rändern
-Wir wollen kein Briefpapier bedrucken lassen, soll mit dem eigenen Drucker bedruckbar sein
Die Schriftart CG Omega sollte installiert sein, für die korrekte Darstellung.

```html
<!DOCTYPE html>
<html lang="de">
<head>
<meta charset="utf-8">
<title>Briefpapier Kanzlei Velmar</title>
<link href="https://fonts.googleapis.com/css2?family=Tenor+Sans&display=swap" rel="stylesheet">
<style>
  :root {
    --brand-blue: #22407f;
    --text-dark: #2b2b2b;
    --rule: #3a3a3a;
    --paper: #ffffff;
  }
  html, body {
    margin: 0;
    padding: 0;
    overflow: hidden;
  }
  body {
    width: 872px;
    height: 1200px;
    background: var(--paper);
    font-family: "Tenor Sans", "Optima", sans-serif;
    color: var(--text-dark);
  }
  .letterhead {
    position: relative;
    width: 872px;
    height: 1200px;
    background: var(--paper);
  }
  .brand {
    position: absolute;
    left: 70px;
    top: 64px;
    display: flex;
    align-items: center;
    gap: 12px;
  }
  .brand-dot {
    width: 14px;
    height: 14px;
    border-radius: 50%;
    background: var(--brand-blue);
  }
  .brand-name {
    font-size: 32px;
    line-height: 1;
    color: var(--brand-blue);
    letter-spacing: 0.2px;
  }
  .partners {
    position: absolute;
    right: 34px;
    top: 40px;
    text-align: right;
    font-size: 13.5px;
    line-height: 17px;
  }
  .partner + .partner { margin-top: 37px; }
  .partner-name {
    font-size: 17px;
    line-height: 21px;
    font-weight: bold;
    color: var(--brand-blue);
  }
  .contact {
    position: absolute;
    left: 80px;
    top: 174px;
    font-size: 13.5px;
    line-height: 17px;
  }
  .contact-group + .contact-group { margin-top: 14px; }
  .contact-group.mail { margin-top: 20px; }
  .contact-row {
    display: flex;
    align-items: center;
    gap: 14px;
  }
  .contact-row svg {
    width: 12px;
    height: 12px;
    flex: none;
    fill: var(--brand-blue);
  }
  .contact-row .spacer { width: 12px; flex: none; }
  .fold-mark {
    position: absolute;
    left: 0;
    top: 400px;
    width: 33px;
    border-top: 1px solid var(--rule);
  }
  .footer-rule {
    position: absolute;
    left: 60px;
    width: 751px;
    top: 1129px;
    border-top: 1px solid var(--rule);
  }
  .footer {
    position: absolute;
    left: 40px;
    right: 40px;
    top: 1148px;
    text-align: center;
    font-size: 12.3px;
    line-height: 15px;
  }
  .footer .sep { margin: 0 6px; }
</style>
</head>
<body>
<div class="letterhead">

  <div class="brand">
    <span class="brand-dot"></span>
    <span class="brand-name">Kanzlei Velmar</span>
  </div>

  <div class="partners">
    <div class="partner">
      <div class="partner-name">Tarek Velmar</div>
      <div>Diplom-Kaufmann</div>
      <div>Steuerberater</div>
    </div>
    <div class="partner">
      <div class="partner-name">Emre Velmar</div>
      <div>Rechtsanwalt</div>
      <div>Fachanwalt für Steuerrecht</div>
    </div>
  </div>

  <div class="contact">
    <div class="contact-group">
      <div class="contact-row">
        <svg viewBox="0 0 12 12" aria-hidden="true"><path d="M6 0.5a4 4 0 0 0-4 4c0 3 4 7 4 7s4-4 4-7a4 4 0 0 0-4-4zm0 5.5a1.5 1.5 0 1 1 0-3 1.5 1.5 0 0 1 0 3z"/></svg>
        <span>Lindenweg 14</span>
      </div>
      <div class="contact-row"><span class="spacer"></span><span>71034 Talheim</span></div>
    </div>
    <div class="contact-group">
      <div class="contact-row">
        <svg viewBox="0 0 12 12" aria-hidden="true"><path d="M2.5 1l2 2.2-1 1.2c.6 1.4 1.7 2.5 3.1 3.1l1.2-1 2.2 2-1.2 1.5C5.6 9.8 2.2 6.4 1 3.2z"/></svg>
        <span>Telefon : 07031 - 554210</span>
      </div>
      <div class="contact-row">
        <svg viewBox="0 0 12 12" aria-hidden="true"><path d="M3 1h6v3H8V2H4v2H3zM1.5 4.5h9a.5.5 0 0 1 .5.5v4H9v2H3V9H1V5a.5.5 0 0 1 .5-.5zM4 7.5v2.5h4V7.5z"/></svg>
        <span>Telefax : 07031 - 554212</span>
      </div>
    </div>
    <div class="contact-group mail">
      <div class="contact-row">
        <svg viewBox="0 0 12 12" aria-hidden="true"><path d="M1 2.5h10v7H1zm1 1v.3l4 2.6 4-2.6v-.3zm0 1.5v3.5h8V5L6 7.6z"/></svg>
        <span>mail@kanzlei-velmar.de</span>
      </div>
      <div class="contact-row">
        <svg viewBox="0 0 12 12" aria-hidden="true"><path d="M6 1a5 5 0 1 0 0 10A5 5 0 0 0 6 1zm-.6 1.1C4.8 2.9 4.4 4 4.3 5.4H2.1a4 4 0 0 1 3.3-3.3zm1.2 0a4 4 0 0 1 3.3 3.3H7.7C7.6 4 7.2 2.9 6.6 2.1zM5.3 5.4C5.4 4.2 5.6 3 6 2.3c.4.7.6 1.9.7 3.1zM2.1 6.6h2.2c.1 1.4.5 2.5 1.1 3.3a4 4 0 0 1-3.3-3.3zm3.2 0h1.4c-.1 1.2-.3 2.4-.7 3.1-.4-.7-.6-1.9-.7-3.1zm2.4 0h2.2a4 4 0 0 1-3.3 3.3c.6-.8 1-1.9 1.1-3.3z"/></svg>
        <span>www.kanzlei-velmar.de</span>
      </div>
    </div>
  </div>

  <div class="fold-mark"></div>

  <div class="footer-rule"></div>
  <div class="footer">
    <div>Bankverbindung | Kanzlei Velmar GbR<span class="sep">•</span>Nordmark Bank AG<span class="sep">•</span>IBAN : DE12 3004 0050 0417 2236 00<span class="sep">•</span>BIC : NOMADEFFXXX</div>
    <div>Umsatzsteuer-ID | DE214507392</div>
  </div>

</div>
</body>
</html>
```